Billboard Design for Equipment Rental Business

We need a billboard design for our equipment rental business called Brindlewood Equipment Company. We are based in Georgia. We rent construction tools, equipment, and dumpsters. We currently have a design but feel like we could get something better. Our phone number is 912-730-2591 and our website is www.brindlewoodequipment-example.com

```html
<!DOCTYPE html>
<html lang="en">
<head>
<meta charset="utf-8">
<title>Brindlewood Equipment Company — Billboard</title>
<link rel="stylesheet" href="https://fonts.googleapis.com/css2?family=Oswald:wght@500;600;700&display=swap">
<style>
  :root {
    --page-bg: #e6e6e6;
    --sky-blue: #2f5d7c;
    --sky-deep: #1e3f5a;
    --sunset-orange: #e0733f;
    --sunset-glow: #f3a24a;
    --dirt-brown: #5a3a24;
    --dirt-dark: #3a2416;
    --machine-amber: #e89a2a;
    --machine-deep: #8a4a18;
    --machine-steel: #4a4440;
    --brand-yellow: #fbc123;
    --ink: #1a1a1a;
    --white: #ffffff;
    --text-shadow: rgba(60, 25, 10, 0.75);
  }
  * { margin: 0; padding: 0; box-sizing: border-box; }
  html, body {
    width: 928px;
    height: 1200px;
    overflow: hidden;
    background: var(--page-bg);
    font-family: "Oswald", sans-serif;
  }
  .canvas {
    position: relative;
    width: 928px;
    height: 1200px;
    display: flex;
    align-items: center;
    justify-content: center;
  }
  .billboard {
    position: relative;
    width: 860px;
    height: 344px;
    overflow: hidden;
    box-shadow: 0 18px 28px -14px rgba(0, 0, 0, 0.35);
  }
  .billboard__sky {
    position: absolute;
    inset: 0;
    background:
      linear-gradient(180deg, rgba(0,0,0,0) 70%, var(--dirt-brown) 86%, var(--dirt-dark) 100%),
      radial-gradient(ellipse at 58% 76%, var(--sunset-glow) 0%, rgba(243,162,74,0) 42%),
      linear-gradient(110deg, var(--sky-deep) 0%, var(--sky-blue) 22%, var(--sunset-orange) 55%, #d8683c 100%);
  }
  .hero-photo {
    position: absolute;
    left: 232px;
    top: 16px;
    width: 392px;
    height: 312px;
    border-radius: 46% 54% 10% 10% / 40% 40% 8% 8%;
    background:
      radial-gradient(ellipse at 70% 62%, var(--machine-amber) 0%, rgba(232,154,42,0.85) 28%, rgba(232,154,42,0) 62%),
      radial-gradient(ellipse at 22% 72%, var(--machine-steel) 0%, rgba(74,68,64,0.8) 26%, rgba(74,68,64,0) 55%),
      radial-gradient(ellipse at 50% 30%, rgba(138,74,24,0.85) 0%, rgba(138,74,24,0) 60%),
      linear-gradient(180deg, rgba(138,74,24,0) 55%, var(--dirt-brown) 85%, var(--dirt-dark) 100%);
  }
  .headline {
    position: absolute;
    top: 30px;
    left: 45px;
    right: 45px;
    display: flex;
    justify-content: space-between;
    align-items: center;
    color: var(--white);
    font-weight: 700;
    font-size: 54px;
    line-height: 1;
    letter-spacing: 2px;
    text-transform: uppercase;
    text-shadow: 2px 2px 0 var(--text-shadow);
  }
  .headline__dot {
    width: 10px;
    height: 10px;
    border-radius: 50%;
    background: var(--white);
  }
  .brand-badge {
    position: absolute;
    left: 59px;
    top: 106px;
    width: 205px;
    height: 205px;
    border-radius: 50%;
    background: var(--brand-yellow);
    display: flex;
    flex-direction: column;
    align-items: center;
    justify-content: center;
    color: var(--ink);
    font-weight: 600;
    text-align: center;
  }
  .brand-badge__name { font-size: 29px; line-height: 1.05; letter-spacing: 0.5px; }
  .brand-badge__sub { font-size: 11.5px; letter-spacing: 0.8px; margin-top: 4px; }
  .contact {
    position: absolute;
    right: 45px;
    top: 108px;
    text-align: right;
    color: var(--white);
    text-shadow: 2px 2px 0 var(--text-shadow);
  }
  .contact__label { font-size: 27px; font-weight: 600; line-height: 1.1; }
  .contact__phone { font-size: 54px; font-weight: 600; line-height: 1.08; letter-spacing: -0.5px; }
  .contact__web { font-size: 20px; font-weight: 500; line-height: 1.25; letter-spacing: -0.3px; }
</style>
</head>
<body>
<main class="canvas">
  <section class="billboard">
    <div class="billboard__sky" role="img" aria-label="Dramatic blue and orange sunset sky above mounds of brown dirt"></div>
    <div class="hero-photo" role="img" aria-label="Photo of a yellow excavator with its bucket digging into a dirt mound"></div>

    <h1 class="headline">
      <span>Tools</span><span class="headline__dot"></span><span>Equipment</span><span class="headline__dot"></span><span>Dumpsters</span>
    </h1>

    <div class="brand-badge">
      <span class="brand-badge__name">BRINDLEWOOD</span>
      <span class="brand-badge__sub">EQUIPMENT COMPANY</span>
    </div>

    <div class="contact">
      <p class="contact__label">CALL US</p>
      <p class="contact__phone">912-730-2591</p>
      <p class="contact__web">brindlewoodequipment-example.com</p>
    </div>
  </section>
</main>
</body>
</html>
```